Meridian Rest Supply Needs Business Card

Looking for a very nice looking business card. Creative but not extravagant. We sell beds and pillows across the U.S. and need something professional but catchy. I have attached the logo.

Name : Dale Fenwick
Title : President
Phone : (800) 417-2964
Email: sleep@quorvana.com
Website: www.quorvana.com

Can be single-sided or double-sided
horizontal or vertical

Can use Blues/Greys

Target Market(s)

Mass Market

Industry/Entity Type

Retail

Contact Information for Business Card

Name : Dale Fenwick
Title : President
Phone : (800) 417-2964
Email: sleep@quorvana.com
Website: www.quorvana.com

Requirements
Must have
• Clean, Modern, Smooth
• Can use Blues/Greys
• On the other side without the information - have something simple like www.quorvana.com or our logo
Nice to have
• Surprise me
Should not have
• Nothing crazy, nothing cluttered

```html
<!DOCTYPE html>
<html lang="en">
<head>
<meta charset="utf-8">
<title>Meridian Rest Supply – Business Card</title>
<link rel="stylesheet" href="https://fonts.googleapis.com/css2?family=Poiret+One&family=Roboto+Slab:wght@300;400&display=swap">
<style>
  :root {
    --stage-bg: #d9d9d9;
    --card-blue: #3399c9;
    --ink-dark: #1f1f24;
    --ink-light: #f2f6f8;
  }
  * { box-sizing: border-box; margin: 0; padding: 0; }
  html, body {
    width: 1200px;
    height: 800px;
    overflow: hidden;
    background: var(--stage-bg);
  }
  .stage {
    width: 1200px;
    height: 800px;
    display: flex;
    align-items: center;
    justify-content: center;
  }
  .card {
    position: relative;
    width: 840px;
    height: 480px;
    border-radius: 40px;
    background: var(--card-blue);
    display: flex;
    flex-direction: column;
    align-items: center;
  }
  .website {
    margin-top: 150px;
    font-family: "Poiret One", sans-serif;
    font-size: 76px;
    letter-spacing: 1px;
    color: var(--ink-dark);
    line-height: 1;
  }
  .website .domain { color: var(--ink-light); }
  .person {
    margin-top: 34px;
    text-align: center;
    font-family: "Roboto Slab", serif;
  }
  .person-name {
    font-size: 30px;
    font-weight: 400;
    color: var(--ink-light);
    line-height: 1.1;
  }
  .person-title {
    font-size: 20px;
    font-weight: 300;
    color: var(--ink-dark);
    margin-top: 2px;
  }
  .contact {
    margin-top: 38px;
    display: flex;
    gap: 22px;
    font-family: "Roboto Slab", serif;
    font-size: 20px;
    font-weight: 300;
    color: var(--ink-light);
  }
  .contact-item {
    display: flex;
    align-items: center;
    gap: 8px;
  }
  .contact-icon { width: 26px; height: 26px; flex: none; }
</style>
</head>
<body>
<main class="stage">
  <section class="card" aria-label="Business card, Meridian Rest Supply">
    <p class="website">www.<span class="domain">quorvana</span>.com</p>
    <div class="person">
      <p class="person-name">Dale Fenwick</p>
      <p class="person-title">President</p>
    </div>
    <div class="contact">
      <span class="contact-item">
        <svg class="contact-icon" viewBox="0 0 26 26" aria-hidden="true">
          <circle cx="13" cy="13" r="11.5" fill="none" stroke="#1f1f24" stroke-width="1.6"/>
          <path d="M9.5 7.5c-1.2.6-1.6 2-1 3.6 1.1 3 3.4 5.6 6.4 6.9 1.5.6 2.9.2 3.5-1l-2.2-1.8-1.4 1c-1.6-.8-3-2.3-3.7-4l1-1.4-1.6-2.3z" fill="none" stroke="#1f1f24" stroke-width="1.3" stroke-linejoin="round"/>
        </svg>
        (800) 417-2964
      </span>
      <span class="contact-item">
        <svg class="contact-icon" viewBox="0 0 26 26" aria-hidden="true">
          <rect x="2" y="6" width="22" height="15" fill="none" stroke="#1f1f24" stroke-width="1.6"/>
          <path d="M2 6l11 9 11-9M2 21l8-7M24 21l-8-7" fill="none" stroke="#1f1f24" stroke-width="1.3"/>
        </svg>
        sleep@quorvana.com
      </span>
    </div>
  </section>
</main>
</body>
</html>
```